BrightKeel Business Card Contest

We are looking for a modern business card that catches attention and is unique. Attached is the brand guide and logo files. Please note that the back side (not the side with our name and info) with be UV raise printed, so have fun with the design there. We want to include Name, Title, Phone number, email, website.

Contact Information for Business Card

Please see project description

```html
<!DOCTYPE html>
<html lang="en">
<head>
<meta charset="utf-8">
<title>BrightKeel Business Card</title>
<link href="https://fonts.googleapis.com/css2?family=Montserrat:wght@400;500;600&display=swap" rel="stylesheet">
<style>
  :root {
    --backdrop: #585c5f;
    --card: #111517;
    --white: #ffffff;
    --text-soft: #cfd3d6;
    --blue: #2a7fd4;
    --orange: #f08a1c;
  }
  html, body {
    margin: 0;
    padding: 0;
    width: 1200px;
    height: 1200px;
    overflow: hidden;
    background: var(--backdrop);
    font-family: "Montserrat", Arial, sans-serif;
  }
  .business-card {
    position: absolute;
    left: 165px;
    top: 348px;
    width: 870px;
    height: 507px;
    border-radius: 27px;
    background: var(--card);
    overflow: hidden;
  }
  .accent-lines {
    position: absolute;
    inset: 0;
    width: 870px;
    height: 507px;
  }
  .brand-name {
    position: absolute;
    left: 45px;
    top: 272px;
    margin: 0;
    font-size: 66px;
    font-weight: 500;
    line-height: 1;
    letter-spacing: -0.5px;
    color: var(--white);
  }
  .divider {
    position: absolute;
    left: 434px;
    top: 80px;
    width: 3px;
    height: 397px;
    background: linear-gradient(to bottom, rgba(240,138,28,0), var(--orange) 50%, rgba(240,138,28,0));
  }
  .person-name {
    position: absolute;
    left: 480px;
    top: 135px;
    margin: 0;
    font-size: 45px;
    font-weight: 600;
    line-height: 1;
    color: var(--white);
  }
  .person-title {
    position: absolute;
    left: 482px;
    top: 188px;
    margin: 0;
    font-size: 13.5px;
    font-weight: 400;
    letter-spacing: 4px;
    color: var(--blue);
    line-height: 1;
  }
  .contact-list {
    position: absolute;
    left: 484px;
    top: 310px;
    margin: 0;
    padding: 0;
    list-style: none;
  }
  .contact-item {
    display: flex;
    align-items: center;
    height: 45px;
    font-size: 27px;
    color: var(--text-soft);
  }
  .contact-icon {
    width: 24px;
    height: 24px;
    margin-right: 12px;
    flex: none;
  }
</style>
</head>
<body>
  <div class="business-card">
    <svg class="accent-lines" viewBox="0 0 870 507" aria-hidden="true">
      <defs>
        <linearGradient id="fadeOrange" x1="0" y1="0" x2="1" y2="1">
          <stop offset="0" stop-color="#f08a1c"/>
          <stop offset="1" stop-color="#f08a1c" stop-opacity="0"/>
        </linearGradient>
        <linearGradient id="fadeBlue" x1="1" y1="0" x2="0" y2="1">
          <stop offset="0" stop-color="#2a7fd4" stop-opacity="0.2"/>
          <stop offset="1" stop-color="#2a7fd4"/>
        </linearGradient>
        <linearGradient id="fadeOrangeUp" x1="0" y1="1" x2="1" y2="0">
          <stop offset="0" stop-color="#f08a1c" stop-opacity="0"/>
          <stop offset="1" stop-color="#f08a1c"/>
        </linearGradient>
        <linearGradient id="fadeBlueUp" x1="0" y1="1" x2="1" y2="0">
          <stop offset="0" stop-color="#2a7fd4"/>
          <stop offset="1" stop-color="#2a7fd4" stop-opacity="0.2"/>
        </linearGradient>
      </defs>
      <line x1="180" y1="0" x2="45" y2="155" stroke="url(#fadeOrange)" stroke-width="2"/>
      <line x1="97" y1="60" x2="0" y2="180" stroke="url(#fadeBlue)" stroke-width="2"/>
      <line x1="870" y1="279" x2="735" y2="439" stroke="url(#fadeOrangeUp)" stroke-width="2"/>
      <line x1="817" y1="391" x2="726" y2="507" stroke="url(#fadeBlueUp)" stroke-width="2"/>
    </svg>

    <p class="brand-name">BrightKeel</p>

    <div class="divider"></div>

    <h1 class="person-name">Jordan Reyes</h1>
    <p class="person-title">DIRECTOR OF OPERATIONS</p>

    <ul class="contact-list">
      <li class="contact-item">
        <svg class="contact-icon" viewBox="0 0 24 24" aria-hidden="true">
          <circle cx="12" cy="12" r="12" fill="#2a7fd4"/>
          <path d="M8.2 6.5c.4-.3 1-.3 1.3.1l1.3 1.8c.3.4.2.9-.1 1.2l-.8.7c.6 1.3 1.6 2.4 2.9 3.1l.7-.8c.3-.4.9-.4 1.2-.1l1.8 1.3c.4.3.4.9.1 1.3l-.8.9c-.5.5-1.3.7-2 .4-3-1.2-5.2-3.5-6.3-6.5-.3-.7-.1-1.5.4-2z" fill="#111517"/>
        </svg>
        <span>+1 555 987 2210</span>
      </li>
      <li class="contact-item">
        <svg class="contact-icon" viewBox="0 0 24 24" aria-hidden="true">
          <circle cx="12" cy="12" r="12" fill="#2a7fd4"/>
          <rect x="6" y="8" width="12" height="8.5" rx="1" fill="#111517"/>
          <path d="M6.5 8.6 12 12.6l5.5-4" stroke="#2a7fd4" stroke-width="1.2" fill="none"/>
        </svg>
        <span>jordan@brightkeel</span>
      </li>
      <li class="contact-item">
        <svg class="contact-icon" viewBox="0 0 24 24" aria-hidden="true">
          <circle cx="12" cy="12" r="12" fill="#2a7fd4"/>
          <g stroke="#111517" stroke-width="1.2" fill="none">
            <circle cx="12" cy="12" r="6"/>
            <ellipse cx="12" cy="12" rx="2.6" ry="6"/>
            <line x1="6" y1="12" x2="18" y2="12"/>
            <line x1="7" y1="9" x2="17" y2="9"/>
            <line x1="7" y1="15" x2="17" y2="15"/>
          </g>
        </svg>
        <span>brightkeel</span>
      </li>
    </ul>
  </div>
</body>
</html>
```